Design a Website Mockup for A Vehicle Dealership

This contest is for a web design for a vehicle dealership. It requires 2 pages.

A complete brief is attached but let me know if you need any further details.

I have sealed it so that nobody else can see your great ideas!!

Thank you and good luck!

```html
<!DOCTYPE html>
<html lang="en">
<head>
<meta charset="utf-8">
<title>Riverton Motors – Dealership Website Pages</title>
<link rel="stylesheet" href="https://fonts.googleapis.com/css2?family=Arimo:wght@400;700&display=swap">
<style>
  :root {
    --canvas: #e4ecef;
    --ink-dark: #141414;
    --bar-dark: rgba(20,20,20,0.85);
    --tab-dark: #2a2a2a;
    --accent-red: #b8242a;
    --accent-red-bright: #d43a3a;
    --text-light: #ffffff;
    --text-muted: #9a9a9a;
    --panel-glass: rgba(255,255,255,0.22);
    --panel-edge: rgba(255,255,255,0.55);
    --field-bg: #f4f4f4;
    --field-edge: #8c8c8c;
    --form-grey: #9a9a9a;
    --form-grey-dark: #7d7d7d;
    --footer-dark: #1c1c1c;
  }
  * { box-sizing: border-box; margin: 0; padding: 0; }
  html, body { width: 1200px; height: 1200px; overflow: hidden; }
  body {
    background: var(--canvas);
    font-family: "Arimo", Arial, sans-serif;
    position: relative;
  }

  /* ---------- Home page ---------- */
  .home-page {
    position: absolute; left: 40px; top: 40px;
    width: 1120px; height: 620px; overflow: hidden;
    background: var(--ink-dark);
  }
  .home-hero {
    position: absolute; inset: 0;
    background:
      radial-gradient(ellipse 30% 40% at 33% 45%, #4a4d52 0%, rgba(40,42,46,0) 70%),
      radial-gradient(ellipse 22% 35% at 58% 50%, #3d4045 0%, rgba(40,42,46,0) 70%),
      radial-gradient(ellipse 40% 30% at 50% 95%, #2a2c30 0%, rgba(20,20,20,0) 70%),
      linear-gradient(180deg, #6a6e72 0%, #2b2d31 35%, #1a1b1e 70%, #0f1012 100%);
  }
  .top-accent {
    position: absolute; left: 0; top: 0; width: 100px; height: 5px;
    background: var(--accent-red);
  }
  .site-bar {
    position: absolute; left: 100px; right: 0; top: 0; height: 58px;
    background: var(--bar-dark);
    border-bottom: 1px solid #3a3a3a;
  }
  .tagline {
    position: absolute; left: 60px; top: 19px;
    color: var(--text-muted); font-size: 16px;
  }
  .main-nav { position: absolute; right: 0; top: 0; display: flex; height: 58px; }
  .main-nav a {
    display: block; width: 150px; line-height: 58px; text-align: center;
    color: var(--text-light); font-weight: 700; font-size: 21px;
    text-decoration: none; border-left: 1px solid #4a4a4a;
    background: var(--tab-dark);
  }
  .main-nav a.is-active {
    color: var(--accent-red-bright); font-weight: 400;
    background: #3c3c3c;
  }

  .inventory-search {
    position: absolute; left: 740px; top: 150px; width: 316px; height: 305px;
    background: var(--panel-glass);
    border: 1px solid var(--panel-edge); border-radius: 10px;
    padding: 16px 38px;
  }
  .inventory-search h2 {
    color: #e8e8e8; font-size: 22px; font-weight: 400; text-align: center;
    margin-bottom: 12px;
  }
  .condition-row { display: flex; gap: 26px; margin-bottom: 14px; color: #f0f0f0; font-size: 16px; }
  .condition-row label { display: flex; align-items: center; gap: 8px; }
  .check-box {
    width: 15px; height: 15px; background: #f4f4f4; border: 1px solid #777;
    display: inline-flex; align-items: center; justify-content: center;
  }
  .search-select {
    position: relative; height: 26px; margin-bottom: 9px;
    background: var(--field-bg); border: 1px solid var(--field-edge);
    color: #222; font-size: 16px; line-height: 24px; padding-left: 4px;
  }
  .search-select::after {
    content: ""; position: absolute; right: 0; top: 0; width: 20px; height: 24px;
    background: #e2e2e2; border-left: 1px solid #bbb;
  }
  .select-arrow { position: absolute; right: 5px; top: 9px; z-index: 1; }
  .search-submit {
    display: block; margin: 10px auto 0; width: 96px; height: 24px;
    background: var(--accent-red); color: #fff; border: 1px solid #7a1317;
    font-family: inherit; font-weight: 700; font-size: 16px;
  }

  .dealer-contact {
    position: absolute; right: 36px; top: 530px;
    color: var(--text-light); font-weight: 700; font-size: 20px;
    display: grid; grid-template-columns: auto auto; column-gap: 28px; row-gap: 8px;
  }
  .dealer-contact .address { grid-column: 1 / 3; font-size: 21px; justify-self: end; margin-bottom: 4px; }
  .dealer-contact .label { font-weight: 400; text-align: right; }

  /* ---------- Contact page ---------- */
  .contact-page {
    position: absolute; left: 40px; top: 690px;
    width: 360px; height: 480px; overflow: hidden;
    background: #3b3b3b;
    font-size: 6px;
  }
  .contact-bar {
    height: 20px; background: var(--footer-dark); position: relative;
    border-top: 2px solid var(--accent-red);
  }
  .contact-bar .tagline-small { position: absolute; left: 56px; top: 5px; color: #777; font-size: 6px; }
  .contact-bar nav { position: absolute; right: 40px; top: 0; display: flex; }
  .contact-bar nav a {
    color: #fff; font-weight: 700; font-size: 8px; text-decoration: none;
    padding: 0 12px; line-height: 18px; border-left: 1px solid #444;
  }
  .contact-header { position: relative; height: 132px; }
  .map-area {
    position: absolute; inset: 0;
    background: linear-gradient(135deg, #8a8a8a 0%, #b5b5b5 40%, #9c9c9c 70%, #7e7e7e 100%);
  }
  .brand-name {
    position: absolute; left: 14px; top: 48px;
    color: #fff; font-weight: 700; font-size: 17px;
    display: flex; align-items: center; gap: 6px;
  }
  .brand-name::before { content: ""; width: 10px; height: 10px; background: #fff; }
  .dealer-callout {
    position: absolute; left: 196px; top: 22px; width: 146px;
    background: #f6f6f6; border: 1px solid #bbb; padding: 5px 7px;
    color: #333; line-height: 9px;
  }
  .dealer-callout h3 { color: var(--accent-red); font-size: 8px; text-align: right; }
  .dealer-callout .callout-address { text-align: right; font-weight: 700; margin-bottom: 2px; }
  .dealer-callout .row { display: flex; justify-content: space-between; }
  .dealer-callout .directions { text-align: center; color: #888; }

  .contact-form {
    margin: 14px 24px 0; height: 205px;
    background: var(--form-grey); border: 1px solid #b3b3b3;
    padding: 8px 18px;
  }
  .contact-form h2 {
    color: var(--accent-red); font-size: 8px; font-weight: 700;
    text-transform: uppercase; border-bottom: 1px solid #b3b3b3;
    padding-bottom: 3px; margin-bottom: 5px;
  }
  .form-row { display: flex; align-items: flex-start; margin-bottom: 4px; }
  .form-row span { width: 60px; text-align: right; padding-right: 6px; color: #f0f0f0; line-height: 8px; }
  .form-field { width: 150px; height: 8px; background: #ececec; border: 1px solid #777; }
  .form-field.is-textarea { height: 38px; }
  .form-field.is-select { width: 40px; }
  .form-foot { display: flex; justify-content: space-between; align-items: center; margin-top: 6px; color: #eee; }
  .form-foot label { display: flex; align-items: center; gap: 3px; }
  .tiny-check { width: 6px; height: 6px; background: #eee; border: 1px solid #666; }
  .form-submit { width: 22px; height: 8px; background: var(--accent-red); border: none; }

  .contact-footer {
    position: absolute; left: 0; right: 0; bottom: 0; height: 118px;
    background: var(--footer-dark); color: #bdbdbd;
    padding: 8px 14px; display: flex; gap: 10px; line-height: 8px;
  }
  .contact-footer h4 { color: #fff; font-size: 7px; margin-bottom: 2px; }
  .footer-col { width: 95px; }
  .footer-col.hours h4 + p + p + p { margin-bottom: 6px; }
  .signup-field { width: 60px; height: 8px; background: #3d3d3d; margin-top: 4px; }
  .map-thumb {
    width: 34px; height: 22px; margin-top: 4px;
    background: linear-gradient(135deg, #d9d4c6, #bfc9b5);
  }
  .follow-row { display: flex; align-items: center; gap: 4px; margin-top: 26px; }
  .follow-row i { width: 8px; height: 8px; background: #6a6a6a; display: block; }
  .copyright {
    position: absolute; left: 14px; right: 14px; bottom: 5px;
    display: flex; justify-content: space-between; color: #777; font-size: 5px;
  }
</style>
</head>
<body>

<section class="home-page" aria-label="Home page">
  <div class="home-hero" role="img" aria-label="Photo of a car interior with steering wheel, dashboard and gear shift"></div>
  <div class="top-accent"></div>
  <header class="site-bar">
    <p class="tagline">You're only a few clicks away from your new car</p>
    <nav class="main-nav">
      <a href="#" class="is-active">Home</a>
      <a href="#">Inventory</a>
      <a href="#">Contact</a>
    </nav>
  </header>

  <form class="inventory-search">
    <h2>Inventory Search:</h2>
    <div class="condition-row">
      <label><span class="check-box"></span>New</label>
      <label><span class="check-box"><svg width="11" height="11" viewBox="0 0 11 11"><path d="M1 6 L4 9 L10 1" fill="none" stroke="#222" stroke-width="1.6"/></svg></span>Pre-owned</label>
    </div>
    <div class="search-select">--all years--<svg class="select-arrow" width="9" height="6"><path d="M0 0 H9 L4.5 6Z" fill="#333"/></svg></div>
    <div class="search-select">--all makes--<svg class="select-arrow" width="9" height="6"><path d="M0 0 H9 L4.5 6Z" fill="#333"/></svg></div>
    <div class="search-select">--all models--<svg class="select-arrow" width="9" height="6"><path d="M0 0 H9 L4.5 6Z" fill="#333"/></svg></div>
    <div class="search-select">--all body styles--<svg class="select-arrow" width="9" height="6"><path d="M0 0 H9 L4.5 6Z" fill="#333"/></svg></div>
    <div class="search-select">--any price--<svg class="select-arrow" width="9" height="6"><path d="M0 0 H9 L4.5 6Z" fill="#333"/></svg></div>
    <button class="search-submit" type="button">submit</button>
  </form>

  <div class="dealer-contact">
    <span class="address">48 Harbor Lane Riverton NY 10480</span>
    <span class="label">Showroom Phone:</span><span>1555-010.22.40</span>
    <span class="label">Service Phone:</span><span>1555-010.22.41</span>
    <span class="label">Fax:</span><span>1555-010.22.42</span>
  </div>
</section>

<section class="contact-page" aria-label="Contact page">
  <header class="contact-bar">
    <p class="tagline-small">You're only a few clicks away from your new car</p>
    <nav><a href="#">Home</a><a href="#">Inventory</a></nav>
  </header>

  <div class="contact-header">
    <div class="map-area" role="img" aria-label="Street map around the dealership"></div>
    <div class="brand-name">Riverton Motors</div>
    <div class="dealer-callout">
      <h3>This Dealership</h3>
      <p class="callout-address">48 Harbor Lane Riverton NY</p>
      <p class="row"><span>Showroom Phone</span><span>1555-010.22.40</span></p>
      <p class="row"><span>Service Phone</span><span>1555-010.22.41</span></p>
      <p class="row"><span>Fax</span><span>1555-010.22.42</span></p>
      <p class="directions">Get directions</p>
    </div>
  </div>

  <form class="contact-form">
    <h2>What can we do to help you?</h2>
    <div class="form-row"><span>Subject</span><div class="form-field"></div></div>
    <div class="form-row"><span>Message</span><div class="form-field is-textarea"></div></div>
    <h2>How can we get in touch with you?</h2>
    <div class="form-row"><span>First Name</span><div class="form-field"></div></div>
    <div class="form-row"><span>Last Name</span><div class="form-field"></div></div>
    <div class="form-row"><span>Preferred Contact</span><div class="form-field is-select"></div></div>
    <div class="form-row"><span>E-mail</span><div class="form-field"></div></div>
    <div class="form-row"><span>Day Phone</span><div class="form-field"></div></div>
    <div class="form-foot">
      <label><span class="tiny-check"></span>Send copy to my e-mail</label>
      <button class="form-submit" type="button"></button>
    </div>
  </form>

  <footer class="contact-footer">
    <div class="footer-col hours">
      <h4>Showroom Hours:</h4>
      <p>Monday to Friday - 9am to 8pm</p>
      <p>Saturday - 9am to 6pm</p>
      <p>Sunday - closed</p>
      <h4>Service Hours:</h4>
      <p>Monday to Friday - 8am to 6pm</p>
      <p>Saturday - 8am to 2pm</p>
      <p>Sunday - closed</p>
    </div>
    <div class="footer-col">
      <h4>Sign Up for Our Special Offers</h4>
      <div class="signup-field"></div>
      <div class="signup-field"></div>
    </div>
    <div class="footer-col">
      <h4>Click for Driving Directions</h4>
      <div class="map-thumb" role="img" aria-label="Small map thumbnail"></div>
      <div class="follow-row"><span>Find Us on:</span><i></i><i></i><i></i></div>
    </div>
    <div class="copyright"><span>© 2024 Riverton Motors. All rights reserved.</span><span>Site by Studio</span></div>
  </footer>
</section>

</body>
</html>
```